Web Design job - Condo Debts Collection Business needs a Web Design

I need a site for a client, who works with condo debts collection, and ensure all revenues provided by condo fees will be always available to the building manager of condo on a specific date, regardless of defaults.
I have the visual identity (logo, slogan and colors) of the company, and some requirements on layout (kind of slider, menu options, phone number on a noble position, etc) - maybe I can do a sketch, but I like the idea of give some freedom to designer.

*** PLEASE, we have no interest in templates. We want something new***

Target Market(s)

I have two targets for this design: - Condominium's building manager. This target is looking for a solution to overdue debts on it's condo. - Residents on condominiums. This target wants to live in a better place, where their neighbors pay their condominium fees on time.

Number of Pages Required

1 page

Requirements
Must have
• - Slider with title, some short text related, a nice image (I prefer happy and/or peaceful family, people doing business, happy friends, and so on).
• - I have a special attention to menu. I'm looking for one I can have a nice effect, more elegant, charming, kind of innovative.
• - Phone number on the top (or clearly visible).
• - Member log in area or icon on the top (or clearly visible).
• - News/articles area.
• - Modern fonts, with good quality, sans-serif on areas where reading is more intensive (prefer Google web-fonts).
• - Colors specified on attached files.
Nice to have
• - Clear background color, cause it's better to read larger texts (like articles). Dark backgrounds makes reading difficult.
• - A site with effects (like shadows, lines, curves, gradients, lights) is usually pretty.
• - I pay attention on beautiful footers.
Should not have
• - Images with a lot of money (I don't sell richness, I sell tranquility, peace, harmony, safety).
• - Poor menu.

```html
<!DOCTYPE html>
<html lang="en">
<head>
<meta charset="utf-8">
<title>Condara — Condominium Collection</title>
<link href="https://fonts.googleapis.com/css2?family=Lobster&family=Roboto:wght@400;500;700&display=swap" rel="stylesheet">
<style>
:root{
  --gold:#e0a526;
  --gold-light:#f0bf2c;
  --gold-dark:#c98c12;
  --ink:#1f1f1f;
  --text:#555;
  --muted:#888;
  --dark:#232323;
  --footer:#2b2b2b;
  --line:#e6e6e6;
  --soft:#f3f3f3;
  --white:#fff;
}
*{margin:0;padding:0;box-sizing:border-box}
html,body{width:1200px;height:3041px;overflow:hidden}
body{font-family:'Roboto',sans-serif;color:var(--text);background:var(--white);position:relative}
.script{font-family:'Lobster',cursive;font-weight:400}
.abs{position:absolute}

/* top bar */
.topbar{position:absolute;left:0;top:0;width:1200px;height:40px;background:var(--dark);color:#ddd;font-size:13px}
.topbar .contact{position:absolute;left:99px;top:12px;display:flex;gap:14px;align-items:center}
.topbar .contact span{display:flex;align-items:center;gap:7px}
.topbar .sep{color:#777}
.member-btn{position:absolute;left:956px;top:0;width:143px;height:40px;background:var(--gold);color:#fff;font-size:13px;font-weight:500;display:flex;align-items:center;justify-content:center;gap:7px;text-transform:uppercase}

/* header */
.header{position:absolute;left:0;top:40px;width:1200px;height:118px;background:#fff}
.brand{position:absolute;left:99px;top:36px;display:flex;align-items:center;gap:10px;font-size:40px;font-weight:700;color:var(--ink);letter-spacing:-.5px}
.brand .mark{width:40px;height:40px;background:var(--gold)}
.nav{position:absolute;left:618px;top:0;height:118px;display:flex;align-items:center;gap:0;font-size:14px;font-weight:500;color:var(--ink);text-transform:uppercase}
.nav a{color:inherit;text-decoration:none;padding:0 14px;position:relative;height:118px;display:flex;align-items:center}
.nav a.active::before,.nav a.active::after{content:"";position:absolute;left:50%;transform:translateX(-50%);border-left:20px solid transparent;border-right:20px solid transparent}
.nav a.active::before{top:10px;border-bottom:34px solid var(--gold)}
.nav a.active::after{bottom:10px;border-top:34px solid var(--gold)}

/* hero */
.hero{position:absolute;left:0;top:158px;width:1200px;height:622px}
.hero-title{position:absolute;left:99px;top:128px;font-size:72px;color:#fff}
.hero-text{position:absolute;left:99px;top:226px;font-size:21px;font-weight:500;color:#fff;line-height:31px;width:440px}
.btn{display:flex;align-items:center;justify-content:center;gap:8px;background:linear-gradient(90deg,var(--gold-light),var(--gold));color:#fff;border-radius:30px;font-weight:500;text-transform:uppercase}
.hero-btn{position:absolute;left:99px;top:308px;width:237px;height:47px;font-size:18px}
.arrow{position:absolute;top:228px;width:30px;height:30px;display:flex;align-items:center;justify-content:center}

/* section titles */
.sec-title{position:absolute;left:0;width:1200px;text-align:center}
.sec-title .ghost{position:absolute;left:0;width:1200px;top:-20px;font-size:84px;color:rgba(0,0,0,.07)}
.sec-title h2{position:relative;font-size:44px;color:#111}
.sec-lead{position:absolute;left:250px;width:700px;text-align:center;font-size:13px;line-height:24px;color:#555}

/* services */
.card{position:absolute;top:1013px;width:231px;height:305px;background:#fff;border:1px solid var(--line);border-bottom:3px solid var(--gold);text-align:center}
.card svg{margin-top:34px}
.card h3{margin-top:22px;font-size:15px;font-weight:500;color:#222;text-transform:uppercase}
.card p{margin:14px auto 0;width:185px;font-size:12px;line-height:22px;color:#777}
.card .more{margin-top:10px;font-size:12px;font-weight:500;color:var(--gold);text-transform:uppercase}

/* articles */
.articles{position:absolute;left:0;top:1409px;width:1200px;height:741px;background:linear-gradient(180deg,#f1f1f1,#f7f7f7)}
.feature{position:absolute;left:99px;top:1583px;width:495px;height:430px;background:#fff;box-shadow:0 2px 8px rgba(0,0,0,.2)}
.feature .photo{width:495px;height:290px;background:linear-gradient(135deg,#c9b69a,#e3d7c6 45%,#8b8f99)}
.feature h3{margin:34px 0 0 28px;font-size:20px;font-weight:500;color:#222}
.feature p{margin:16px 28px 0;font-size:12px;line-height:22px;color:#777}
.post{position:absolute;left:630px;width:471px;height:196px;background:#fff;border:1px solid var(--line)}
.post .photo{position:absolute;left:0;top:0;width:166px;height:194px}
.post h4{position:absolute;left:194px;top:18px;width:250px;font-size:16px;font-weight:500;line-height:23px;color:#222}
.post .date{position:absolute;left:194px;top:76px;font-size:12px;color:var(--gold);display:flex;gap:6px;align-items:center}
.post p{position:absolute;left:194px;top:104px;width:255px;font-size:11.5px;line-height:22px;color:#777}
.all-btn{position:absolute;left:488px;top:2078px;width:221px;height:46px;font-size:14px}

/* contact */
.contact-sec{position:absolute;left:0;top:2150px;width:1200px;height:587px}
.info-title{position:absolute;left:142px;top:2348px;font-size:34px;color:#fff}
.info-list{position:absolute;left:142px;top:2412px;color:#fff;font-size:15px;line-height:24px}
.info-row{display:flex;gap:18px;margin-bottom:12px}
.info-row svg{flex:none;margin-top:4px}
.hours{display:grid;grid-template-columns:120px 20px auto;line-height:28px}
.form-card{position:absolute;left:624px;top:2203px;width:477px;height:458px;background:#fff;box-shadow:0 2px 10px rgba(0,0,0,.15)}
.form-card h2{text-align:center;margin-top:26px;font-size:40px;color:#111}
.field{position:absolute;left:48px;width:381px;height:44px;border:1px solid #ddd;border-radius:3px;font-size:13px;color:#666;display:flex;align-items:center;gap:14px;padding-left:16px}
.field.msg{height:88px;align-items:flex-start;padding-top:14px}
.submit{position:absolute;left:48px;top:372px;width:381px;height:44px;background:linear-gradient(90deg,var(--gold-light),var(--gold));color:#fff;font-size:14px;font-weight:500;display:flex;align-items:center;justify-content:center;text-transform:uppercase}

/* footer */
.footer{position:absolute;left:0;top:2737px;width:1200px;height:304px;background:var(--footer);color:#eee}
.footer .brand{position:absolute;left:0;width:1200px;top:52px;justify-content:center;color:#fff;font-size:42px}
.socials{position:absolute;left:0;width:1200px;top:152px;display:flex;justify-content:center;gap:14px}
.socials span{width:36px;height:36px;border:2px solid #fff;border-radius:50%}
.fnav{position:absolute;left:0;width:1200px;top:2948px;margin-top:-2737px;display:flex;justify-content:center;gap:16px;font-size:14px}
.fnav i{font-style:normal;color:#999}
.copy{position:absolute;left:0;width:1200px;top:248px;text-align:center;font-size:14px}
</style>
</head>
<body>

<div class="topbar">
  <div class="contact">
    <span><svg width="12" height="12" viewBox="0 0 24 24" fill="#fff"><path d="M6.6 10.8a15 15 0 0 0 6.6 6.6l2.2-2.2a1 1 0 0 1 1-.25 11.4 11.4 0 0 0 3.6.6 1 1 0 0 1 1 1V20a1 1 0 0 1-1 1A17 17 0 0 1 3 4a1 1 0 0 1 1-1h3.5a1 1 0 0 1 1 1c0 1.25.2 2.45.6 3.6a1 1 0 0 1-.25 1z"/></svg>(+1) 555 010 4400</span>
    <span class="sep">|</span>
    <span><svg width="13" height="11" viewBox="0 0 24 18" fill="#fff"><path d="M0 0h24v2L12 10 0 2zM0 5l12 8 12-8v13H0z"/></svg>info@condarasupport.com</span>
  </div>
  <div class="member-btn"><svg width="10" height="12" viewBox="0 0 10 12" fill="#fff"><rect x="0" y="5" width="10" height="7" rx="1"/><path d="M2 5V3.5a3 3 0 0 1 6 0V5" stroke="#fff" stroke-width="1.6" fill="none"/></svg>Member Login</div>
</div>

<header class="header">
  <div class="brand"><span class="mark"></span>condara</div>
  <nav class="nav">
    <a class="active">Home</a><a>About Us</a><a>Services</a><a>News</a><a>Contact Us</a>
    <a><svg width="14" height="14" viewBox="0 0 24 24" fill="none" stroke="#222" stroke-width="3"><circle cx="10" cy="10" r="7"/><path d="M15 15l7 7"/></svg></a>
  </nav>
</header>

<section class="hero">
  <svg class="abs" style="left:0;top:0" width="1200" height="622" viewBox="0 0 1200 622">
    <defs>
      <linearGradient id="heroSky" x1="0" y1="0" x2="0" y2="1">
        <stop offset="0" stop-color="#8a8a78"/><stop offset=".35" stop-color="#c9c08a"/><stop offset=".55" stop-color="#6f7a3d"/><stop offset="1" stop-color="#3f4a22"/>
      </linearGradient>
    </defs>
    <polygon points="0,0 1200,0 1200,492 600,622 0,492" fill="var(--gold)"/>
    <polygon points="0,0 1200,0 1200,478 600,604 0,478" fill="url(#heroSky)" role="img" aria-label="Family walking hand in hand through a sunlit meadow by a river"/>
    <path d="M586 556l14 12 14-12M586 568l14 12 14-12" stroke="#555" stroke-width="2.5" fill="none"/>
  </svg>
  <div class="arrow" style="left:28px"><svg width="10" height="16" viewBox="0 0 10 16"><path d="M8 2L2 8l6 6" stroke="#fff" stroke-width="2.5" fill="none"/></svg></div>
  <div class="arrow" style="left:1142px"><svg width="10" height="16" viewBox="0 0 10 16"><path d="M2 2l6 6-6 6" stroke="#fff" stroke-width="2.5" fill="none"/></svg></div>
  <div class="hero-title script">Condara</div>
  <div class="hero-text">Nemo enim ipsam voluptatem quia voluptas sit aspernatur aut odit aut fugit</div>
  <div class="btn hero-btn">Member Log In <svg width="16" height="16" viewBox="0 0 16 16"><circle cx="8" cy="8" r="8" fill="#fff"/><path d="M6 4.5L9.5 8 6 11.5" stroke="var(--gold)" stroke-width="2" fill="none"/></svg></div>
</section>

<div class="sec-title" style="top:852px"><div class="ghost script">Our Services</div><h2 class="script">Our Services</h2></div>
<p class="sec-lead" style="top:926px">Neque porro quisquam est, qui dolorem ipsum quia dolor sit amet, consectetur, adipisci velit, sed quia non numquam eius modi tempora incidunt ut labore et dolore magnam aliquam quaerat voluptatem.</p>

<div class="card" style="left:99px">
  <svg width="62" height="62" viewBox="0 0 62 62" fill="none" stroke="var(--gold)" stroke-width="2.5"><circle cx="31" cy="20" r="12"/><path d="M31 13v14M27 17h6a3 3 0 0 1 0 6h-4"/><path d="M4 34l10 20h10l8-8M58 34L48 54H38l-8-8"/></svg>
  <h3>Debt Collection</h3>
  <p>Duis aute irure dolor in repen derewit in voltate velit esse cillum dolore eu fugiat nulla partur voluptate velit esse.</p>
</div>
<div class="card" style="left:357px">
  <svg width="62" height="62" viewBox="0 0 62 62" fill="none" stroke="var(--gold)" stroke-width="2.5"><rect x="10" y="4" width="34" height="50"/><path d="M17 16h20M17 24h20M17 32h12"/><circle cx="44" cy="46" r="10"/><path d="M44 41v10"/></svg>
  <h3>Invoice Checking</h3>
  <p>Duis aute irure dolor in repen derewit in voltate velit esse cillum dolore eu fugiat nulla partur voluptate velit esse.</p>
  <div class="more">Read More ›</div>
</div>
<div class="card" style="left:612px">
  <svg width="62" height="62" viewBox="0 0 62 62" fill="none" stroke="var(--gold)" stroke-width="2.5"><rect x="8" y="8" width="46" height="32"/><path d="M4 46h54M16 18h14M16 26h20"/><rect x="36" y="14" width="12" height="10"/></svg>
  <h3>Insolvency Services</h3>
  <p>Duis aute irure dolor in repen derewit in voltate velit esse cillum dolore eu fugiat nulla partur voluptate velit esse.</p>
</div>
<div class="card" style="left:870px">
  <svg width="62" height="62" viewBox="0 0 62 62" fill="none" stroke="var(--gold)" stroke-width="2.5"><rect x="10" y="4" width="42" height="54"/><circle cx="31" cy="26" r="11"/><path d="M31 15v11h11M18 46h26"/></svg>
  <h3>Recovery of NPLs</h3>
  <p>Duis aute irure dolor in repen derewit in voltate velit esse cillum dolore eu fugiat nulla partur voluptate velit esse.</p>
</div>

<section class="articles"></section>
<div class="sec-title" style="top:1472px"><div class="ghost script">Latest Articles</div><h2 class="script">Latest Articles</h2></div>

<article class="feature">
  <div class="photo" role="img" aria-label="Business people shaking hands across an office desk"></div>
  <h3>Lorem ipsum dolor sit, consectetur</h3>
  <p>At vero eos et accusamus et iusto odio dignissimos ducimus qui blanditiis praesentium voluptatum vcbcb deleniti atque corrupti</p>
</article>
<article class="post" style="top:1583px">
  <div class="photo" role="img" aria-label="Couple reviewing documents with an advisor" style="background:linear-gradient(135deg,#7d7a74,#c7c1b6 50%,#5b5f66)"></div>
  <h4>Nemo enim ipsam volutem odit voluptasit aspernatur odit</h4>
  <div class="date"><svg width="11" height="11" viewBox="0 0 11 11" fill="var(--gold)"><rect x="0" y="2" width="11" height="9"/></svg>Jun 28, 2018</div>
  <p>Neque porro quisquam est, qui dolorem ipsum quia dolor sit amet, consectetur, adipisci velit, sed quia non numquam eius modi</p>
</article>
<article class="post" style="top:1818px">
  <div class="photo" role="img" aria-label="Family relaxing together on the grass in a park" style="background:linear-gradient(135deg,#c9c15a,#7f9a3a 55%,#4c6a26)"></div>
  <h4>Nemo enim ipsam volutem odit voluptasit aspernatur odit</h4>
  <div class="date"><svg width="11" height="11" viewBox="0 0 11 11" fill="var(--gold)"><rect x="0" y="2" width="11" height="9"/></svg>July 08, 2018</div>
  <p>Neque porro quisquam est, qui dolorem ipsum quia dolor sit amet, consectetur, adipisci velit, sed quia non numquam eius modi</p>
</article>
<div class="btn all-btn">View All Blog Post <svg width="14" height="14" viewBox="0 0 16 16"><circle cx="8" cy="8" r="8" fill="#fff"/><path d="M6 4.5L9.5 8 6 11.5" stroke="var(--gold)" stroke-width="2" fill="none"/></svg></div>

<section class="contact-sec">
  <svg class="abs" style="left:0;top:0" width="1200" height="587" viewBox="0 0 1200 587">
    <defs>
      <linearGradient id="goldField" x1="0" y1="0" x2="0" y2="1">
        <stop offset="0" stop-color="#e2a424"/><stop offset=".7" stop-color="#d99e2a"/><stop offset="1" stop-color="#c89a4a"/>
      </linearGradient>
    </defs>
    <rect width="1200" height="587" fill="#f7f7f7"/>
    <polygon points="0,10 355,178 1200,26 1200,587 0,587" fill="url(#goldField)" role="img" aria-label="Father carrying his child on his shoulders in a golden field"/>
  </svg>
</section>
<div class="info-title script">Contact Information</div>
<div class="info-list">
  <div class="info-row"><svg width="14" height="16" viewBox="0 0 14 18" fill="#fff"><path d="M7 0a7 7 0 0 1 7 7c0 5-7 11-7 11S0 12 0 7a7 7 0 0 1 7-7zm0 4a3 3 0 1 0 0 6 3 3 0 0 0 0-6z"/></svg><div>412 Harbor Lane, Fairview,<br>US 50218.</div></div>
  <div class="info-row"><svg width="14" height="14" viewBox="0 0 24 24" fill="#fff"><path d="M6.6 10.8a15 15 0 0 0 6.6 6.6l2.2-2.2a1 1 0 0 1 1-.25 11.4 11.4 0 0 0 3.6.6 1 1 0 0 1 1 1V20a1 1 0 0 1-1 1A17 17 0 0 1 3 4a1 1 0 0 1 1-1h3.5a1 1 0 0 1 1 1c0 1.25.2 2.45.6 3.6a1 1 0 0 1-.25 1z"/></svg>(+1) 555 010 4400</div>
  <div class="info-row"><svg width="14" height="12" viewBox="0 0 24 18" fill="#fff"><path d="M0 0h24v2L12 10 0 2zM0 5l12 8 12-8v13H0z"/></svg>info@condarasupport.com</div>
  <div class="info-row"><svg width="14" height="14" viewBox="0 0 16 16"><circle cx="8" cy="8" r="7" fill="none" stroke="#fff" stroke-width="2"/><path d="M8 4v4h3" stroke="#fff" stroke-width="2" fill="none"/></svg>
    <div class="hours"><span>Monday - Friday</span><span>:</span><span>9am to 4:30pm.</span><span>Saturday</span><span>:</span><span>10am to 03pm.</span><span>Sunday</span><span>:</span><span>Closed</span></div>
  </div>
</div>

<div class="form-card">
  <h2 class="script">Contact Us</h2>
  <div class="field" style="top:98px"><svg width="11" height="12" viewBox="0 0 12 12" fill="#666"><circle cx="6" cy="3" r="3"/><path d="M0 12a6 6 0 0 1 12 0z"/></svg>Name</div>
  <div class="field" style="top:153px"><svg width="11" height="11" viewBox="0 0 24 24" fill="#666"><path d="M6.6 10.8a15 15 0 0 0 6.6 6.6l2.2-2.2a1 1 0 0 1 1-.25 11.4 11.4 0 0 0 3.6.6 1 1 0 0 1 1 1V20a1 1 0 0 1-1 1A17 17 0 0 1 3 4a1 1 0 0 1 1-1h3.5a1 1 0 0 1 1 1c0 1.25.2 2.45.6 3.6a1 1 0 0 1-.25 1z"/></svg>Phone</div>
  <div class="field" style="top:208px"><svg width="12" height="10" viewBox="0 0 24 18" fill="#666"><path d="M0 0h24v2L12 10 0 2zM0 5l12 8 12-8v13H0z"/></svg>Email Address</div>
  <div class="field msg" style="top:263px"><svg width="11" height="11" viewBox="0 0 12 12" fill="#666"><path d="M0 12l1-4 7-7 3 3-7 7z"/></svg>Message</div>
  <div class="submit">Submit Now!</div>
</div>

<footer class="footer">
  <div class="brand"><span class="mark" style="width:42px;height:42px;background:var(--gold)"></span>condara</div>
  <div class="socials"><span></span><span></span><span></span><span></span><span></span><span></span></div>
  <div class="fnav" style="top:211px;margin-top:0"><span>Home</span><i>|</i><span>About Us</span><i>|</i><span>Services</span><i>|</i><span>News</span><i>|</i><span>Blog</span><i>|</i><span>FAQ</span><i>|</i><span>Contact</span><i>|</i><span>Privacy Policy</span></div>
  <div class="copy">Copyrights © 2018 Condara. All Rights Reserved.</div>
</footer>

</body>
</html>
```